A5 & A3 Size flyer for OPEN NIGHT - Adult Education

We need a A5 & A3 formatted flyer for our upcoming OPEN NIGHT on Thursday, 17th November 2016 at our Kelmswood campus. A3 for poster to display and A5 for flyers.

We are one of Victoria's leading private Reconised Training Organisations based in Melbourne, Victoria, Australia who specialise in the training of nationally recognised training courses in Pathology, Individual Support (Ageing, Home & Community, Disability), Allied Health Assistance, Health Services Assistance, Disability & Ageing Support.

The purpose of our open night is to gain prospective students for 2017 courses and the soul purpose of this flyer is to promote via emails, postal mail and hard copy drop offs to prospective clients, employers and our partnered networks for exposure.

The final design should reflect the colour scheme & style we have used in the attached already promoted designs. Should include our logo, address, event details, website and social media buttons (Facebook, Instagram, Youtube, Twitter, Pinterest & LinkedIn) Should be in line with our overall branding, as per our website www.brightwellcareskills.edu.au and ensure it is bold and engaging for promotional purposes.

Please also see our event listing for which ahs further information you may be able to use: https://bcsinfoevening16.ticketnook.com.au

If you ahve any questions please send through a message!

Target Market(s)

Prospective students, employer organisations workforce

Industry/Entity Type

Adult

Colors
f37122
f78f20
ffc214
ffffff

Requirements
Must have
• See project description

```html
<!DOCTYPE html>
<html lang="en">
<head>
<meta charset="utf-8">
<title>Brightwell Care Skills – Open Night</title>
<link rel="stylesheet" href="https://fonts.googleapis.com/css2?family=Montserrat:wght@500;600&family=Open+Sans:wght@400;600;700&display=swap">
<style>
  :root {
    --orange: #f37122;
    --orange-mid: #f78f20;
    --yellow: #ffc214;
    --white: #ffffff;
    --charcoal: #3d3d3d;
    --ink: #333333;
    --page: #f2f2f2;
  }
  * { box-sizing: border-box; margin: 0; padding: 0; }
  html, body { width: 907px; height: 1200px; overflow: hidden; background: var(--page); }
  body { font-family: "Open Sans", Arial, sans-serif; color: var(--ink); }

  .flyer { position: relative; width: 907px; height: 1200px; background: var(--white); overflow: hidden; }

  .brand { position: absolute; left: 48px; top: 60px; width: 280px; }
  .brand-mark { width: 150px; height: 150px; border-radius: 50%; background: var(--orange); margin: 0 0 26px 40px; }
  .brand-name { font-family: "Open Sans", Arial, sans-serif; font-weight: 600; font-size: 34px; line-height: 1.05; color: var(--orange); }
  .brand-id { font-size: 9px; color: var(--charcoal); margin-top: 8px; margin-left: 90px; }

  .hero-photo { position: absolute; left: 360px; top: 0; width: 547px; height: 430px;
    background: linear-gradient(120deg, #eef1f4 0%, #d9dde2 45%, #2b2b2e 70%, #c9cdd2 100%); }

  .band-orange { position: absolute; left: 0; top: 432px; width: 907px; height: 20px; background: var(--orange); }
  .band-yellow { position: absolute; left: 0; top: 456px; width: 907px; height: 5px; background: var(--yellow); }

  .title { position: absolute; left: 0; width: 907px; top: 478px; text-align: center;
    font-family: "Montserrat", Arial, sans-serif; font-weight: 600; font-size: 84px; letter-spacing: 2px; color: var(--orange); line-height: 1; }

  .date-pill { position: absolute; left: 72px; top: 582px; width: 764px; height: 52px; border-radius: 26px;
    background: var(--charcoal); color: var(--white); text-align: center;
    font-family: "Montserrat", Arial, sans-serif; font-weight: 500; font-size: 32px; line-height: 52px; }

  .intro { position: absolute; top: 652px; width: 350px; font-size: 14px; line-height: 1.45; color: var(--ink); }
  .intro-left { left: 72px; }
  .intro-right { left: 480px; }

  .courses { position: absolute; top: 752px; left: 0; width: 907px; height: 220px; display: flex; }
  .courses-col { list-style: none; padding: 18px 30px 0 70px; }
  .courses-col.left { width: 463px; background: var(--orange); color: var(--white); }
  .courses-col.right { width: 444px; background: var(--yellow); color: var(--ink); padding-left: 40px; }
  .courses-col li { position: relative; font-size: 13.5px; line-height: 1.3; margin-bottom: 11px; padding-left: 18px; }
  .courses-col li::before { content: ""; position: absolute; left: 0; top: 4px; width: 9px; height: 9px; border-radius: 50%; background: var(--yellow); }
  .courses-col.right li::before { background: var(--orange); }
  .courses-col .note { display: block; }
  .courses-col strong { font-weight: 700; }

  .happening { position: absolute; left: 72px; top: 998px; }
  .happening h2 { font-family: "Open Sans", Arial, sans-serif; font-weight: 700; font-size: 24px; color: var(--orange); margin-bottom: 8px; }
  .happening ul { list-style: none; padding-left: 6px; }
  .happening li { position: relative; font-size: 13.5px; line-height: 1.55; padding-left: 18px; }
  .happening li::before { content: ""; position: absolute; left: 0; top: 6px; width: 9px; height: 9px; border-radius: 50%; background: var(--orange); }

  .phone { position: absolute; left: 540px; top: 1000px; width: 300px; height: 50px; border: 2px solid #cfcfcf; border-radius: 25px; display: flex; align-items: center; }
  .phone-icon { width: 50px; height: 50px; margin-left: -2px; border-radius: 25px; background: var(--charcoal); display: flex; align-items: center; justify-content: center; }
  .phone-number { font-family: "Montserrat", Arial, sans-serif; font-weight: 600; font-size: 30px; color: var(--orange); margin-left: 10px; }
  .website { position: absolute; left: 520px; top: 1066px; font-weight: 700; font-size: 17px; color: var(--ink); }

  .footer-bar { position: absolute; left: 0; top: 1098px; width: 907px; height: 102px; }
  .follow { position: absolute; left: 580px; top: 1140px; display: flex; align-items: center; gap: 10px; color: var(--white); font-weight: 700; font-size: 14px; }
  .follow .label { margin-right: 14px; }
  .social-dot { width: 28px; height: 28px; border-radius: 50%; background: var(--orange); }
</style>
</head>
<body>
<main class="flyer">
  <div class="brand">
    <div class="brand-mark"></div>
    <div class="brand-name">brightwell<br>care skills</div>
    <div class="brand-id">TOID 40718</div>
  </div>

  <div class="hero-photo" role="img" aria-label="Photo of two smiling students in black uniform polos sitting at a classroom desk"></div>

  <div class="band-orange"></div>
  <div class="band-yellow"></div>

  <h1 class="title">OPEN NIGHT</h1>
  <div class="date-pill">17th November ,Thursday 2016</div>

  <p class="intro intro-left">Are you looking for a career change? Not sure what to do once high school has finished? Or simply wanting to UpSkill?</p>
  <p class="intro intro-right">Come along and join us at our Open Night - explore our campus, get all your questions answered and learn what career and course options are available to you in 2017.</p>

  <section class="courses">
    <ul class="courses-col left">
      <li>HLT37215 Certificate III in Pathology Collection</li>
      <li>HLT33115 Certificate III in Health Services Assistance</li>
      <li>CHC33015 Certificate III in Individual Support (Ageing, Home and Community)</li>
      <li>CHC33015 Certificate III in Individual Support (Disability)</li>
      <li>CHC43015 Certificate IV in Ageing Support</li>
    </ul>
    <ul class="courses-col right">
      <li>CHC43115 Certificate IV in Disability</li>
      <li>HLT33015 Certificate III in Allied Health Assistance</li>
      <li>HLTAID001 - Provide cardiopulmonary resuscitation, HLTAID003 - Provide first aid</li>
      <li>Professional Development Workshops<span class="note">All information regarding Nationally Recognised Training courses above can be found at: <strong>www.vetcourselist.gov.au</strong></span></li>
    </ul>
  </section>

  <section class="happening">
    <h2>What's happening?</h2>
    <ul>
      <li>Lucky Door Prize Giveaways, Goodie Bags</li>
      <li>Refreshments Provided</li>
      <li>Tours of Campus &amp; Facilities</li>
      <li>Chat to Industry Experts &amp; Course Advisors</li>
      <li>See a Live Tutorial Class in Action</li>
    </ul>
  </section>

  <div class="phone">
    <div class="phone-icon">
      <svg width="26" height="26" viewBox="0 0 24 24" aria-hidden="true">
        <path fill="#ffc214" d="M6.6 10.8c1.4 2.8 3.8 5.1 6.6 6.6l2.2-2.2c.3-.3.7-.4 1-.2 1.1.4 2.3.6 3.6.6.6 0 1 .4 1 1V20c0 .6-.4 1-1 1C10.6 21 3 13.4 3 4c0-.6.4-1 1-1h3.5c.6 0 1 .4 1 1 0 1.3.2 2.5.6 3.6.1.3 0 .7-.2 1l-2.3 2.2z"/>
      </svg>
    </div>
    <span class="phone-number">03 9000 4127</span>
  </div>
  <div class="website">www.brightwellcareskills.edu.au</div>

  <svg class="footer-bar" viewBox="0 0 907 102" preserveAspectRatio="none" aria-hidden="true">
    <path fill="#3d3d3d" d="M430 102 C470 40 490 20 560 18 L907 18 L907 102 Z"/>
  </svg>
  <div class="follow">
    <span class="label">Follow us</span>
    <span class="social-dot"></span>
    <span class="social-dot"></span>
    <span class="social-dot"></span>
    <span class="social-dot"></span>
    <span class="social-dot"></span>
  </div>
</main>
</body>
</html>
```